Refresh Application User Interface

Brindlecove wishes to update the look of its business applications. Two representative forms are shown below. Please note, we are not considering changes in functionality or usability. Our goal is a cleaner, more contemporary design.

Industry/Entity Type

Business

```html
<!DOCTYPE html>
<html lang="en">
<head>
<meta charset="utf-8">
<title>Brindlecove – Purchase Order</title>
<link href="https://fonts.googleapis.com/css2?family=Roboto:wght@400;500;700;900&display=swap" rel="stylesheet">
<style>
:root{
  --blue:#0a5aaa;
  --blue-dark:#07498c;
  --green:#8dc05a;
  --green-dark:#7aad48;
  --ink:#222;
  --muted:#555;
  --line:#cfcfcf;
  --panel:#f7f7f7;
  --sub:#f3f3f3;
  --chip:#f1f1f1;
}
*{box-sizing:border-box;margin:0;padding:0}
html,body{width:1200px;height:1182px;overflow:hidden}
body{font-family:'Roboto',sans-serif;color:var(--ink);background:#fff;position:relative}
.abs{position:absolute}
.header{left:0;top:0;width:1200px;height:55px;background:#fff;box-shadow:0 2px 4px rgba(0,0,0,.15);z-index:2}
.brand{left:22px;top:12px;font-size:28px;font-weight:900;color:var(--blue);letter-spacing:-.5px;display:flex;align-items:center;gap:8px}
.brand .dot{width:14px;height:14px;border-radius:50%;background:var(--green)}
.session{left:410px;top:16px;height:22px;display:flex;align-items:center;font-size:12px;color:#333;white-space:nowrap}
.session b{color:var(--blue);font-weight:500}
.session .round{margin:0 14px 0 10px}
.round{width:22px;height:22px;border-radius:50%;background:var(--green);display:flex;align-items:center;justify-content:center;flex:none}
.toplinks{left:828px;top:19px;font-size:12px;color:#333;word-spacing:4px}
.logout{left:1078px;top:9px;width:102px;height:36px;background:var(--green);color:#fff;font-size:11px;font-weight:700;display:flex;align-items:center;justify-content:center;border-radius:2px}
.apps{left:0;top:55px;width:1200px;height:75px;background:#f4f4f4}
.app{top:24px;width:91px;height:31px;border:1px solid #d6d6d6;background:#fff;font-size:13px;display:flex;align-items:center;justify-content:center}
.app.on{background:var(--green);color:#fff;border-color:var(--green)}
.nav{left:0;top:130px;width:1200px;height:40px;background:var(--green);display:flex;align-items:center;padding-left:26px;gap:26px;color:#fff;font-size:13px;font-weight:500}
.title{left:21px;top:193px;font-size:21px;font-weight:700;color:var(--blue)}
.view{top:185px;width:103px;height:36px;background:var(--chip);border:1px solid #e2e2e2;font-size:12px;display:flex;align-items:center;justify-content:center;color:#333}
.view.on{background:var(--blue);color:#fff;border-color:var(--blue)}
.toolbar{left:19px;top:237px;width:1162px;height:46px;background:var(--blue);color:#fff;font-size:12px;font-weight:500}
.tool{top:0;height:46px;width:44px;display:flex;align-items:center;justify-content:center;border-right:1px solid var(--blue-dark)}
.act{top:11px;display:flex;align-items:center;gap:10px}
.act i{width:26px;height:26px;border-radius:50%;background:#fff;display:flex;align-items:center;justify-content:center;font-style:normal;color:var(--green);font-size:16px;border:2px solid #d9ecc6}
.panel{left:19px;top:283px;width:1162px;height:899px;background:var(--panel);box-shadow:0 0 6px rgba(0,0,0,.08)}
.lbl{font-size:12px;font-weight:500;text-align:right;width:200px;color:#222}
.field{width:307px;height:38px;background:#fff;border:1px solid var(--line);border-radius:2px}
.tab{top:668px;height:36px;background:var(--chip);border:1px solid #e0e0e0;font-size:12px;font-weight:500;display:flex;align-items:center;justify-content:center}
.tab.on{background:var(--sub);border-color:var(--sub);color:var(--blue);height:42px}
.sub{left:52px;top:710px;width:1110px;height:442px;background:var(--sub)}
.select{width:307px;height:38px;background:#fff;border:1px solid var(--line);border-radius:2px;font-size:11px;color:#444;display:flex;align-items:center;padding-left:15px}
.select::after{content:"";position:absolute;right:16px;top:17px;border:4px solid transparent;border-top:4px solid #333}
.cta{left:52px;top:1095px;width:1110px;height:57px;background:var(--green);color:#fff;font-size:14px;font-weight:700;display:flex;align-items:center;justify-content:center}
</style>
</head>
<body>
<header class="abs header">
  <div class="abs brand">BRINDLECOVE<span class="dot"></span></div>
  <div class="abs session">
    <span>Logged In As <b>Dana Whitlow</b></span>
    <span class="round"><svg width="12" height="12" viewBox="0 0 12 12"><circle cx="6" cy="6" r="3.5" fill="none" stroke="#fff" stroke-width="2"/></svg></span>
    <span>Current Role <b>Administrator</b></span>
    <span class="round"><svg width="10" height="6"><path d="M0 0h10L5 6z" fill="#fff"/></svg></span>
  </div>
  <div class="abs toplinks">Touch / New Tab / Help / Support</div>
  <div class="abs logout">LOG OUT</div>
</header>

<div class="abs apps">
  <div class="abs app" style="left:22px">Home</div>
  <div class="abs app" style="left:125px">eSource</div>
  <div class="abs app on" style="left:227px">eBuy</div>
  <div class="abs app" style="left:330px">eRequest</div>
  <div class="abs app" style="left:432px">eSell</div>
  <div class="abs app" style="left:535px">eStock</div>
  <div class="abs app" style="left:637px">ePlan</div>
  <div class="abs app" style="left:740px;width:95px">Preferences</div>
</div>

<nav class="abs nav"><span>Orders</span><span>Receipts</span><span>Shipments</span><span>Invoices</span><span>Pricing</span><span>Tables Reports</span><span>Inquiries</span><span>Periodic Tasks</span><span>Workflows</span></nav>

<h1 class="abs title">PURCHASE ORDER</h1>
<div class="abs view on" style="left:732px">Folder Tabs</div>
<div class="abs view" style="left:848px">Lines</div>
<div class="abs view" style="left:962px">Charges</div>
<div class="abs view" style="left:1077px">Notes</div>

<div class="abs toolbar">
  <div class="abs tool" style="left:0"><svg width="12" height="18" viewBox="0 0 12 18"><path d="M3 5v8a3 3 0 0 0 6 0V4a2 2 0 0 0-4 0v9" fill="none" stroke="#fff" stroke-width="1.5"/></svg></div>
  <div class="abs tool" style="left:44px"><svg width="16" height="18"><path d="M2 1h8l4 4v12H2z" fill="none" stroke="#fff" stroke-width="1.3"/><circle cx="9" cy="11" r="3" fill="none" stroke="#fff" stroke-width="1.3"/></svg></div>
  <div class="abs tool" style="left:88px"><svg width="18" height="18"><circle cx="4" cy="9" r="2.5" fill="#fff"/><circle cx="14" cy="3.5" r="2.5" fill="#fff"/><circle cx="14" cy="14.5" r="2.5" fill="#fff"/><path d="M4 9l10-5.5M4 9l10 5.5" stroke="#fff" stroke-width="1.5"/></svg></div>
  <div class="abs tool" style="left:132px"><svg width="20" height="16"><rect x="1" y="4" width="18" height="11" rx="1" fill="#fff"/><rect x="7" y="1" width="6" height="4" fill="none" stroke="#fff" stroke-width="1.5"/><path d="M1 9h18" stroke="#0a5aaa"/></svg></div>
  <div class="abs tool" style="left:176px;font-size:22px;font-weight:700">?</div>
  <div class="abs tool" style="left:220px;width:150px;gap:12px"><svg width="26" height="20"><rect x="1" y="1" width="24" height="18" fill="none" stroke="#fff" stroke-width="1.3"/><circle cx="14" cy="11" r="4" fill="none" stroke="#fff" stroke-width="1.3"/><path d="M17 14l4 4" stroke="#fff" stroke-width="1.3"/></svg>Post Order</div>
  <div class="abs act" style="left:724px"><i>⌕</i>Search</div>
  <div class="abs act" style="left:813px"><i>+</i>New</div>
  <div class="abs act" style="left:894px"><i>✓</i>Apply</div>
  <div class="abs act" style="left:984px"><i>×</i>Delete</div>
  <div class="abs act" style="left:1076px"><i>↩</i>Back</div>
</div>

<main class="abs panel"></main>

<div class="abs lbl" style="left:36px;top:334px">Order#</div><div class="abs field" style="left:253px;top:325px"></div>
<div class="abs lbl" style="left:39px;top:400px">Ship From</div><div class="abs field" style="left:253px;top:390px"></div>
<div class="abs lbl" style="left:39px;top:466px">Harbor Clinical Goods</div><div class="abs field" style="left:253px;top:456px"></div>
<div class="abs lbl" style="left:39px;top:533px">Address</div><div class="abs field" style="left:253px;top:521px"></div>
<div class="abs lbl" style="left:39px;top:600px">City</div><div class="abs field" style="left:253px;top:587px"></div>

<div class="abs lbl" style="left:483px;top:334px">Zip</div><div class="abs field" style="left:699px;top:325px"></div>
<div class="abs lbl" style="left:480px;top:401px">Country</div><div class="abs field" style="left:699px;top:390px"></div>
<div class="abs lbl" style="left:483px;top:467px">State</div><div class="abs field" style="left:699px;top:456px"></div>
<div class="abs lbl" style="left:483px;top:534px">Address</div><div class="abs field" style="left:699px;top:521px"></div>
<div class="abs lbl" style="left:483px;top:600px">Add Contact</div><div class="abs field" style="left:699px;top:587px"></div>

<div class="abs tab" style="left:52px;width:103px">Order info</div>
<div class="abs tab on" style="left:167px;width:103px">Shipping</div>
<div class="abs tab" style="left:281px;width:103px">Payment</div>
<div class="abs tab" style="left:396px;width:103px">Account</div>
<div class="abs tab" style="left:512px;width:130px">Totals / Approval</div>

<section class="abs sub"></section>

<div class="abs lbl" style="left:31px;top:792px">Recevice At</div><div class="abs select" style="left:252px;top:781px">ALCH</div>
<div class="abs lbl" style="left:31px;top:851px">Carrier</div><div class="abs select" style="left:252px;top:840px">Swiftline</div>
<div class="abs lbl" style="left:31px;top:911px">Express Service</div><div class="abs select" style="left:252px;top:900px"></div>
<div class="abs lbl" style="left:31px;top:970px">Fob</div><div class="abs select" style="left:252px;top:959px"></div>
<div class="abs lbl" style="left:31px;top:1030px">Order Ship Rule</div><div class="abs select" style="left:252px;top:1019px">Partials</div>

<div class="abs lbl" style="left:486px;top:792px">Line Ship Rule</div><div class="abs select" style="left:700px;top:781px">Partials</div>
<div class="abs lbl" style="left:486px;top:851px">Request Date</div><div class="abs select" style="left:700px;top:840px">03/20/2018</div>
<div class="abs lbl" style="left:486px;top:911px">Freight Terms</div><div class="abs select" style="left:700px;top:900px">Collect</div>
<div class="abs lbl" style="left:486px;top:970px">Freight Calc</div><div class="abs select" style="left:700px;top:959px"></div>
<div class="abs lbl" style="left:486px;top:1030px">Custmer Ship To</div><div class="abs select" style="left:700px;top:1019px">/</div>

<div class="abs cta">Enter Property Values And Click Apply</div>
</body>
</html>
```